Design a simple and clean PowerPoint slide templates for a Board meeting. The slides should have predominantly white backgrounds and use the brand graphic standards (attached). I'm also attached a PowerPoint master that I don't like, as it's too basic.
The company name is Harborline Weighworks.
It sells, calibrates, services and repairs industrial and commercial scales of all types. In particular, Truck scales, floor scales, counting scales and benchtop scales.
The website is harborlineweighworks.example but this are the old colors, so ignore the logo and colors. We are launching a new logo and new look. Several variations of the logo are available.

```html
<!DOCTYPE html>
<html lang="en">
<head>
<meta charset="utf-8">
<title>Harborline Weighworks – Board Slide Templates</title>
<link href="https://fonts.googleapis.com/css2?family=Poppins:wght@400;500;600;700&display=swap" rel="stylesheet">
<style>
:root{
  --backdrop:#4b4b4b;
  --white:#ffffff;
  --navy:#1b2a4e;
  --band-start:#1f3a58;
  --band-end:#8f6a3c;
  --orange:#f7931e;
  --ink:#2a2a2a;
  --body:#444649;
  --rule:#c9cacd;
  --swoosh:#d3d4d7;
  --photo-dark:#2c3447;
  --photo-warm:#7a4a3e;
  --photo-blue:#1d4a72;
  --photo-light:#d9dee6;
}
*{margin:0;padding:0;box-sizing:border-box}
html,body{width:1200px;height:1109px;overflow:hidden;background:var(--backdrop)}
body{font-family:"Poppins",sans-serif;color:var(--ink)}
.canvas{position:relative;width:1200px;height:1109px;background:var(--backdrop)}
.slide{position:absolute;width:518px;height:292px;background:var(--white);overflow:hidden;box-shadow:0 3px 10px rgba(0,0,0,.35)}
.slide--title{left:56px;top:89px}
.slide--two-col{left:626px;top:89px}
.slide--steps{left:56px;top:409px}
.slide--feature{left:626px;top:409px}
.slide--three-col{left:56px;top:728px}
.slide--closing{left:626px;top:728px}
.wordmark{position:absolute;display:flex;align-items:center;gap:6px}
.wordmark__square{width:10px;height:10px;background:var(--orange)}
.wordmark__name{font-weight:700;color:var(--navy);font-size:14px;line-height:15px;letter-spacing:.5px;text-transform:uppercase}
.footer-url{position:absolute;left:16px;top:270px;font-size:5.6px;letter-spacing:.5px;color:var(--navy);white-space:nowrap}
.footer-rule{position:absolute;top:273px;height:1px;background:var(--rule)}
.page-num{position:absolute;left:488px;top:268px;width:14px;height:14px;border-radius:50%;border:1.5px dashed var(--orange);font-size:5.5px;font-weight:600;display:flex;align-items:center;justify-content:center;color:var(--navy)}
.hero-title{position:absolute;left:16px;top:88px;font-size:34px;line-height:35px;color:var(--navy);font-weight:400}
.hero-title__accent{color:var(--orange);font-weight:600}
.header-art{position:absolute;left:0;top:0}
.sub-title{position:absolute;left:16px;top:14px;font-size:14px;color:var(--white);font-weight:400}
.main-heading{position:absolute;left:16px;top:31px;font-size:16px;font-weight:700;color:var(--orange)}
.intro{position:absolute;left:16px;top:101px;width:290px;font-size:7.6px;line-height:9.2px;font-weight:600;color:var(--ink)}
.col-heading{font-size:8.2px;font-weight:600;color:var(--orange);text-transform:uppercase;margin-bottom:7px}
.col-text{font-size:6.9px;line-height:9.8px;color:var(--body)}
.column{position:absolute;top:154px}
.divider{position:absolute;width:1px;background:var(--rule)}
.steps-photo{position:absolute;left:0;top:0;width:242px;height:238px;border-radius:0 0 120px 0;background:linear-gradient(135deg,#0f2a45,var(--photo-blue) 55%,#5d7690)}
.steps-sub{position:absolute;left:270px;top:14px;font-size:14px;color:var(--ink)}
.steps-heading{position:absolute;left:270px;top:31px;font-size:16px;font-weight:700;color:var(--orange)}
.steps-underline{position:absolute;left:270px;top:55px;width:139px;height:1.5px;background:#8a8b8e}
.steps-intro{position:absolute;left:270px;top:78px;width:215px;font-size:7.6px;line-height:9.2px;font-weight:600}
.step{position:absolute;left:270px;display:flex;align-items:flex-start;gap:6px;width:232px}
.step__dot{flex:0 0 22px;height:22px;border-radius:50%;background:var(--orange);color:var(--white);font-size:7px;font-weight:600;display:flex;align-items:center;justify-content:center}
.step__text{font-size:7px;line-height:10px;color:var(--body);padding-top:1px}
.step-link{position:absolute;left:281px;width:1px;background:var(--rule)}
.feature-photo{position:absolute;left:15px;top:148px;width:88px;height:88px;border:1.5px solid var(--navy);border-radius:5px;background:linear-gradient(135deg,#f3f4f6,#c9ced6)}
.feature-copy{position:absolute;left:116px;top:152px;width:370px}
.closing-photo{position:absolute;left:0;top:0;width:518px;height:194px;background:linear-gradient(180deg,#3b5f86 0%,#1c4474 55%,#123a6a 100%)}
.closing-title{position:absolute;left:0;width:518px;top:142px;text-align:center;font-size:24px;font-weight:500;color:var(--white)}
</style>
</head>
<body>
<main class="canvas">

  <section class="slide slide--title">
    <svg class="header-art" width="518" height="292" viewBox="0 0 518 292">
      <defs>
        <linearGradient id="heroGrad" x1="0" y1="0" x2="1" y2="1">
          <stop offset="0" stop-color="var(--photo-warm)"/>
          <stop offset=".5" stop-color="var(--photo-dark)"/>
          <stop offset="1" stop-color="#1c2233"/>
        </linearGradient>
      </defs>
      <path d="M280 0 C300 95 245 165 166 202 C300 172 430 150 518 190 L518 0 Z" fill="url(#heroGrad)" role="img" aria-label="Photo of a hand placing a steel calibration weight on a scale plate"/>
      <path d="M284 0 C304 100 258 168 190 200" fill="none" stroke="var(--swoosh)" stroke-width="4"/>
      <path d="M166 212 C260 190 330 182 380 180" fill="none" stroke="var(--swoosh)" stroke-width="3"/>
      <path d="M440 170 C480 172 505 182 518 192" fill="none" stroke="var(--swoosh)" stroke-width="4"/>
      <circle cx="377" cy="188" r="67" fill="var(--photo-light)" stroke="var(--orange)" stroke-width="4" role="img" aria-label="Photo of hands measuring a ring with digital calipers"/>
    </svg>
    <div class="wordmark" style="left:16px;top:27px">
      <span class="wordmark__square"></span>
      <span class="wordmark__name">Harborline<br>Weighworks</span>
    </div>
    <h1 class="hero-title">Precision<br>in Every<br><span class="hero-title__accent">Measure</span></h1>
    <div class="footer-url">www.harborlineweighworks.example</div>
    <div class="footer-rule" style="left:160px;width:343px"></div>
  </section>

  <section class="slide slide--two-col">
    <svg class="header-art" width="518" height="120" viewBox="0 0 518 120">
      <defs>
        <linearGradient id="bandA" x1="0" y1="0" x2="1" y2="0">
          <stop offset="0" stop-color="var(--band-start)"/>
          <stop offset="1" stop-color="var(--band-end)"/>
        </linearGradient>
      </defs>
      <path d="M0 0 L208 0 L364 22 L364 52 Q180 62 0 88 Z" fill="url(#bandA)"/>
      <path d="M210 4 L364 16" stroke="var(--swoosh)" stroke-width="3"/>
      <path d="M0 93 Q180 66 364 58" fill="none" stroke="var(--swoosh)" stroke-width="2.5"/>
      <circle cx="448" cy="31" r="85" fill="#8aa0b8" stroke="var(--orange)" stroke-width="4" role="img" aria-label="Photo of an engineer reviewing drawings beside a machine"/>
    </svg>
    <div class="sub-title">Sub Title</div>
    <h2 class="main-heading">Main Heading Here</h2>
    <p class="intro">Lorem ipsum dolor sit amet, consectetur adipiscing elit, sed do eiusmod tempor incididunt ut labore et dolore magna aliqua. Ut enim ad minim veniam, quis nostrud exercitation.</p>
    <div class="column" style="left:16px;width:218px">
      <h3 class="col-heading">Column One Heading</h3>
      <p class="col-text">Lorem Ipsum is simply dummy text of the printing and typesetting industry. Lorem Ipsum has been the industry's standard dummy text ever since 1966, when designers at Typemark and Owen Hartley, the librarian at Foxmoor Print Archive in Eastholm, took a 1914 translation and scrambled it to make dummy text for Typemark's Body Type sheets. It has survived not only many decades.</p>
    </div>
    <div class="divider" style="left:259px;top:153px;height:87px"></div>
    <div class="column" style="left:284px;width:218px">
      <h3 class="col-heading">Column Two Heading</h3>
      <p class="col-text">Lorem Ipsum is simply dummy text of the printing and typesetting industry. Lorem Ipsum has been the industry's standard dummy text ever since 1966, when designers at Typemark and Owen Hartley, the librarian at Foxmoor Print Archive in Eastholm, took a 1914 translation and scrambled it to make dummy text for Typemark's Body Type sheets. It has survived not only many decades.</p>
    </div>
    <div class="footer-url">www.harborlineweighworks.example</div>
    <div class="footer-rule" style="left:160px;width:323px"></div>
    <div class="page-num">1</div>
  </section>

  <section class="slide slide--steps">
    <div class="steps-photo" role="img" aria-label="Close-up photo of a digital caliper measuring a machined steel part"></div>
    <div class="steps-sub">Sub Title</div>
    <h2 class="steps-heading">Main Heading Here</h2>
    <div class="steps-underline"></div>
    <p class="steps-intro">Lorem ipsum dolor sit amet, consectetur adipiscing elit, sed do eiusmod tempor incididunt ut labore et dolore magna aliqua. Ut enim ad minim veniam, quis nostrud exercitation.</p>
    <div class="step-link" style="top:153px;height:17px"></div>
    <div class="step-link" style="top:193px;height:17px"></div>
    <div class="step" style="top:131px"><span class="step__dot">1</span><span class="step__text">Lorem Ipsum is simply dummy text of the printing and typesetting industry.</span></div>
    <div class="step" style="top:170px"><span class="step__dot">2</span><span class="step__text">Lorem Ipsum is simply dummy text of the printing and typesetting industry.</span></div>
    <div class="step" style="top:210px"><span class="step__dot">3</span><span class="step__text">Lorem Ipsum is simply dummy text of the printing and typesetting industry.</span></div>
    <div class="footer-url">www.harborlineweighworks.example</div>
    <div class="footer-rule" style="left:160px;width:323px"></div>
    <div class="page-num">2</div>
  </section>

  <section class="slide slide--feature">
    <svg class="header-art" width="518" height="120" viewBox="0 0 518 120">
      <defs>
        <linearGradient id="bandB" x1="0" y1="0" x2="1" y2="0">
          <stop offset="0" stop-color="var(--band-start)"/>
          <stop offset="1" stop-color="var(--band-end)"/>
        </linearGradient>
      </defs>
      <path d="M0 0 L208 0 L364 22 L364 52 Q180 62 0 88 Z" fill="url(#bandB)"/>
      <path d="M210 4 L364 16" stroke="var(--swoosh)" stroke-width="3"/>
      <path d="M0 93 Q180 66 364 58" fill="none" stroke="var(--swoosh)" stroke-width="2.5"/>
      <circle cx="448" cy="31" r="85" fill="#5f7a70" stroke="var(--orange)" stroke-width="4" role="img" aria-label="Photo of a technician in a hard hat using a control panel"/>
    </svg>
    <div class="sub-title">Sub Title</div>
    <h2 class="main-heading">Main Heading Here</h2>
    <p class="intro" style="top:104px">Lorem ipsum dolor sit amet, consectetur adipiscing elit, sed do eiusmod tempor incididunt ut labore et dolore magna aliqua. Ut enim ad minim veniam, quis nostrud exercitation.</p>
    <div class="feature-photo" role="img" aria-label="Photo of a magnifier over gear technical drawings"></div>
    <div class="feature-copy">
      <h3 class="col-heading">Column One Heading</h3>
      <p class="col-text" style="line-height:8.8px">Contrary to popular belief, Lorem Ipsum is not simply random text. It has roots in a piece of classical Latin literature from 45 BC, making it over 2000 years old. Daniel Everard, a Latin professor at Ridgeview College in Northvale, looked up one of the more obscure Latin words, consectetur, from a Lorem Ipsum passage, and going through the cites of the word in classical literature, discovered the undoubtable source. Lorem Ipsum comes from sections 1.10.32 and 1.10.33 of "de Rebus Mensurae" (The Matters of Measure) by Marcus Vell, written in 45 BC. This book is a treatise on the theory of ethics, very popular during the Renaissance. The first line of Lorem Ipsum, "Lorem ipsum dolor sit amet..", comes from a line in section 1.10.32.</p>
    </div>
    <div class="footer-url">www.harborlineweighworks.example</div>
    <div class="footer-rule" style="left:160px;width:323px"></div>
    <div class="page-num">3</div>
  </section>

  <section class="slide slide--three-col">
    <svg class="header-art" width="518" height="120" viewBox="0 0 518 120">
      <defs>
        <linearGradient id="bandC" x1="0" y1="0" x2="1" y2="0">
          <stop offset="0" stop-color="var(--band-start)"/>
          <stop offset="1" stop-color="var(--band-end)"/>
        </linearGradient>
      </defs>
      <path d="M0 0 L208 0 L364 22 L364 52 Q180 62 0 88 Z" fill="url(#bandC)"/>
      <path d="M210 4 L364 16" stroke="var(--swoosh)" stroke-width="3"/>
      <path d="M0 93 Q180 66 364 58" fill="none" stroke="var(--swoosh)" stroke-width="2.5"/>
      <circle cx="448" cy="31" r="85" fill="#c9b79a" stroke="var(--orange)" stroke-width="4" role="img" aria-label="Photo of hands working over blueprints with a calculator and rulers"/>
    </svg>
    <div class="sub-title">Sub Title</div>
    <h2 class="main-heading">Main Heading Here</h2>
    <p class="intro" style="top:104px">Lorem ipsum dolor sit amet, consectetur adipiscing elit, sed do eiusmod tempor incididunt ut labore et dolore magna aliqua. Ut enim ad minim veniam, quis nostrud exercitation.</p>
    <div class="column" style="left:16px;width:146px">
      <h3 class="col-heading">Column One Heading</h3>
      <p class="col-text">Lorem Ipsum is simply dummy text of the printing and typesetting industry. Lorem Ipsum has been the industry's standard dummy text ever since 1966, when designers at Typemark and Owen Hartley, the librarian at Foxmoor Print Archive in Eastholm.</p>
    </div>
    <div class="divider" style="left:172px;top:152px;height:88px"></div>
    <div class="column" style="left:185px;width:146px">
      <h3 class="col-heading">Column Two Heading</h3>
      <p class="col-text">Lorem Ipsum is simply dummy text of the printing and typesetting industry. Lorem Ipsum has been the industry's standard dummy text ever since 1966, when designers at Typemark and Owen Hartley, the librarian at Foxmoor Print Archive in Eastholm.</p>
    </div>
    <div class="divider" style="left:340px;top:152px;height:88px"></div>
    <div class="column" style="left:355px;width:150px">
      <h3 class="col-heading">Column Three Heading</h3>
      <p class="col-text">Lorem Ipsum is simply dummy text of the printing and typesetting industry. Lorem Ipsum has been the industry's standard dummy text ever since 1966, when designers at Typemark and Owen Hartley, the librarian at Foxmoor Print Archive in Eastholm.</p>
    </div>
    <div class="footer-url">www.harborlineweighworks.example</div>
    <div class="footer-rule" style="left:160px;width:323px"></div>
    <div class="page-num">4</div>
  </section>

  <section class="slide slide--closing">
    <div class="closing-photo" role="img" aria-label="Photo of factory workers in hard hats talking on a plant floor, tinted blue"></div>
    <div class="closing-title">Thank You</div>
    <div class="wordmark" style="left:16px;top:224px">
      <span class="wordmark__square"></span>
      <span class="wordmark__name" style="font-size:16px;line-height:17px">Harborline<br>Weighworks</span>
    </div>
    <div class="footer-rule" style="left:204px;top:256px;width:298px"></div>
    <div class="footer-url" style="left:auto;right:16px;top:270px">www.harborlineweighworks.example</div>
  </section>

</main>
</body>
</html>
```